Flyer Dachdeckerhandwerk
Zielgruppe
Die Steilhang- und Kieselwerk GmbH ist ein renommiertes, inhabergeführtes Familienunternehmen im Dachdeckerhandwerk. Seit über 30 Jahren stehen wir für höchste Qualität, Zuverlässigkeit und fachgerechte Ausführung – von der ersten Beratung bis zur termintreuen Umsetzung auf der Baustelle. Unsere Kunden profitieren von fundiertem Know-how, eingespielten Abläufen und einem starken Team, das langlebige und wirtschaftliche Lösungen realisiert.
Wir bieten eine begrenzte Aktion an und bieten bis 30.06.2026 eine kostenfreie Dachinspektion.
Die Kunden sollen hierfür bei uns anrufen, oder eine Mail mit dem Betreff 'Dachinspektion 2026' senden.
Aufgabenstellung
Unser CI laden wir hoch.
Es soll modern aussehen.

```html
<!DOCTYPE html>
<html lang="de">
<head>
<meta charset="utf-8">
<title>Steilhang- und Kieselwerk GmbH – Flyer Dachinspektion</title>
<link rel="stylesheet" href="https://fonts.googleapis.com/css2?family=Source+Sans+3:wght@400;600;700;800&family=Barlow+Condensed:wght@400;600&display=swap">
<style>
  :root{
    --page-bg:#d6d6d6;
    --dark-green:#0d3a22;
    --brand-green:#0a9a49;
    --box-green-a:#17a856;
    --box-green-b:#0b8f43;
    --footer-a:#0b4d2a;
    --footer-b:#0e3b21;
    --text:#1f2a24;
    --white:#ffffff;
  }
  *{margin:0;padding:0;box-sizing:border-box}
  html,body{width:1200px;height:2250px;overflow:hidden}
  body{background:var(--page-bg);font-family:"Source Sans 3",sans-serif;color:var(--text)}
  .flyer{position:absolute;left:50px;top:347px;width:1100px;height:1556px;background:var(--white);overflow:hidden}
  .sky{position:absolute;inset:0 0 auto 0;height:700px;
    background:radial-gradient(ellipse 520px 420px at 100% 0%,#c9dff0 0%,#e6f0f8 45%,rgba(255,255,255,0) 80%),
               linear-gradient(180deg,#eef5fb 0%,#ffffff 30%)}
  .brand{position:absolute;left:95px;top:82px;display:flex;align-items:center;gap:16px}
  .brand-mark{width:44px;height:44px;background:var(--dark-green)}
  .brand-name{font-size:38px;font-weight:600;color:var(--dark-green);line-height:1}
  .headline{position:absolute;left:100px;top:195px;font-weight:800;font-size:100px;line-height:90px;letter-spacing:-1px;color:var(--dark-green)}
  .headline .accent{color:var(--brand-green)}
  .tagline{position:absolute;left:103px;top:396px;font-size:44px;font-weight:700;color:var(--dark-green)}
  .tagline span{color:var(--brand-green)}
  .intro{position:absolute;left:103px;top:469px;font-size:23.5px;line-height:31px;color:var(--text)}
  .services{position:absolute;left:100px;top:570px;width:477px;height:447px;border-radius:28px;
    background:linear-gradient(135deg,var(--box-green-b) 0%,var(--box-green-a) 60%,var(--box-green-b) 100%);
    color:var(--white);padding:26px 0 0 36px}
  .services h2{font-size:36px;font-weight:700;letter-spacing:.3px;margin-bottom:10px}
  .services ul{list-style:none}
  .services li{display:flex;align-items:flex-start;gap:14px;font-size:24px;font-weight:600;line-height:27px;margin-bottom:13px}
  .services svg{flex:0 0 27px;margin-top:1px}
  .offer{position:absolute;left:618px;top:595px;width:440px}
  .offer-title{font-family:"Barlow Condensed",sans-serif;font-weight:600;font-size:60px;line-height:55px;color:var(--brand-green)}
  .offer-date{font-family:"Barlow Condensed",sans-serif;font-weight:400;font-size:45px;line-height:50px;color:var(--dark-green)}
  .offer-rule{width:160px;height:3px;background:var(--brand-green);margin:14px 0 30px}
  .offer-text{font-size:17.5px;line-height:24.5px;color:var(--text)}
  .offer-text strong{color:var(--brand-green);font-weight:700}
  .photo{position:absolute;left:0;top:1018px;width:1100px;height:363px;
    background:linear-gradient(180deg,#ffffff 0%,#d8c7b0 14%,#a0826a 40%,#4f5a3a 70%,#2a2e22 100%)}
  .footer{position:absolute;left:0;top:1381px;width:1100px;height:175px;
    background:linear-gradient(180deg,var(--footer-a) 0%,var(--footer-b) 100%);color:var(--white)}
  .contact-line{position:absolute;display:flex;align-items:center;gap:16px;font-size:24px;font-weight:600}
  .divider{position:absolute;left:548px;top:42px;width:2px;height:76px;background:rgba(255,255,255,.55)}
  .phone{position:absolute;left:578px;top:28px;display:flex;align-items:center;gap:10px;font-size:60px;font-weight:700;line-height:1}
</style>
</head>
<body>
<main class="flyer">
  <div class="sky" role="img" aria-label="Heller Himmel mit leichten Wolken"></div>

  <div class="brand">
    <span class="brand-mark"></span>
    <span class="brand-name">Steilhang- und Kieselwerk GmbH</span>
  </div>

  <h1 class="headline">WIR SCHÜTZEN,<br><span class="accent">WAS SIE BEDECKT.</span></h1>
  <p class="tagline"><span>S&amp;K</span> moderne Dachsysteme.</p>
  <p class="intro">Unsere Erfahrung im Flachdach-, Steildach- und Begrünungsbau bedeutet<br>Sicherheit für die Immobilie und terminliche Realisation Ihres Bauvorhabens.</p>

  <section class="services">
    <h2>UNSERE LEISTUNGEN</h2>
    <ul>
      <li><svg width="27" height="27" viewBox="0 0 24 24"><circle cx="12" cy="12" r="12" fill="#fff"/><path d="M6.5 12.5l3.6 3.5 7.4-7.6" fill="none" stroke="#0b8f43" stroke-width="3" stroke-linecap="round" stroke-linejoin="round"/></svg>Flachdachabdichtung</li>
      <li><svg width="27" height="27" viewBox="0 0 24 24"><circle cx="12" cy="12" r="12" fill="#fff"/><path d="M6.5 12.5l3.6 3.5 7.4-7.6" fill="none" stroke="#0b8f43" stroke-width="3" stroke-linecap="round" stroke-linejoin="round"/></svg>Dachbegrünung</li>
      <li><svg width="27" height="27" viewBox="0 0 24 24"><circle cx="12" cy="12" r="12" fill="#fff"/><path d="M6.5 12.5l3.6 3.5 7.4-7.6" fill="none" stroke="#0b8f43" stroke-width="3" stroke-linecap="round" stroke-linejoin="round"/></svg>Tiefgaragenabdichtung</li>
      <li><svg width="27" height="27" viewBox="0 0 24 24"><circle cx="12" cy="12" r="12" fill="#fff"/><path d="M6.5 12.5l3.6 3.5 7.4-7.6" fill="none" stroke="#0b8f43" stroke-width="3" stroke-linecap="round" stroke-linejoin="round"/></svg>Spenglerarbeiten &amp;<br>Blechverwahrung</li>
      <li><svg width="27" height="27" viewBox="0 0 24 24"><circle cx="12" cy="12" r="12" fill="#fff"/><path d="M6.5 12.5l3.6 3.5 7.4-7.6" fill="none" stroke="#0b8f43" stroke-width="3" stroke-linecap="round" stroke-linejoin="round"/></svg>Photovoltaik</li>
      <li><svg width="27" height="27" viewBox="0 0 24 24"><circle cx="12" cy="12" r="12" fill="#fff"/><path d="M6.5 12.5l3.6 3.5 7.4-7.6" fill="none" stroke="#0b8f43" stroke-width="3" stroke-linecap="round" stroke-linejoin="round"/></svg>Trapezbleche</li>
      <li><svg width="27" height="27" viewBox="0 0 24 24"><circle cx="12" cy="12" r="12" fill="#fff"/><path d="M6.5 12.5l3.6 3.5 7.4-7.6" fill="none" stroke="#0b8f43" stroke-width="3" stroke-linecap="round" stroke-linejoin="round"/></svg>Lichtkuppeln &amp; RWA Anlagen</li>
      <li><svg width="27" height="27" viewBox="0 0 24 24"><circle cx="12" cy="12" r="12" fill="#fff"/><path d="M6.5 12.5l3.6 3.5 7.4-7.6" fill="none" stroke="#0b8f43" stroke-width="3" stroke-linecap="round" stroke-linejoin="round"/></svg>LUMARA Dachfenster Konfigurator</li>
    </ul>
  </section>

  <section class="offer">
    <h2 class="offer-title">KOSTENFREIE<br>DACHINSPEKTION</h2>
    <p class="offer-date">AKTION BIS 30.06.2026</p>
    <div class="offer-rule"></div>
    <p class="offer-text">Seit mehr als <strong>30 Jahren</strong> ist das Dach unser Zuhause! Hier finden Sie eine Übersicht über von uns realisierte Projekte in modernen Dachsystemen. Dies beinhaltet u.a. Leichtdach, Kiesdach, Gründach mit extensiver und intensiver Begrünung, Bauwerksabdichtung, Trapezblechabdichtung, Lichtkuppel und Dachausstieg, Spenglerarbeiten und Blechverwahrung, Photovoltaik, u.v.m.</p>
  </section>

  <div class="photo" role="img" aria-label="Begrüntes Flachdach mit Solarmodulen und Baum über einer Stadt im Abendlicht"></div>

  <footer class="footer">
    <div class="contact-line" style="left:74px;top:50px">
      <svg width="22" height="22" viewBox="0 0 24 24"><circle cx="12" cy="12" r="11" fill="#17a856"/><path d="M3 12h18M12 2c3 3 3 17 0 20M12 2c-3 3-3 17 0 20" fill="none" stroke="#0d3a22" stroke-width="1.6"/></svg>
      www.sk-kieselwerk.de
    </div>
    <div class="contact-line" style="left:74px;top:84px">
      <svg width="22" height="26" viewBox="0 0 24 28"><path d="M12 1C6.5 1 2.5 5 2.5 10.3 2.5 17 12 27 12 27s9.5-10 9.5-16.7C21.5 5 17.5 1 12 1z" fill="#17a856"/><circle cx="12" cy="10.3" r="3.6" fill="#0d3a22"/></svg>
      Lindenpfad 12 • 55116 Talbrunn
    </div>
    <div class="divider"></div>
    <div class="phone">
      <svg width="32" height="38" viewBox="0 0 24 24"><path d="M6.6 10.8c1.4 2.8 3.8 5.1 6.6 6.6l2.2-2.2c.3-.3.7-.4 1-.2 1.1.4 2.3.6 3.6.6.6 0 1 .4 1 1V20c0 .6-.4 1-1 1C10.6 21 3 13.4 3 4c0-.6.4-1 1-1h3.5c.6 0 1 .4 1 1 0 1.3.2 2.5.6 3.6.1.3 0 .7-.2 1l-2.3 2.2z" fill="#17a856"/></svg>
      06131-4720-0
    </div>
    <div class="contact-line" style="left:584px;top:88px">
      <svg width="22" height="22" viewBox="0 0 24 24"><circle cx="12" cy="12" r="11" fill="#17a856"/><path d="M3 12h18M12 2c3 3 3 17 0 20M12 2c-3 3-3 17 0 20" fill="none" stroke="#0d3a22" stroke-width="1.6"/></svg>
      www.sk-kieselwerk.de
    </div>
  </footer>
</main>
</body>
</html>
```